Business Card Design Project

We need a business card design for our IT Managed Services firm.
Our logo is attached.
More information on our company can be found at:
www.brimvoro.com
Target Market(s)
CEO, President. Mid Size Businesses
Industry/Entity Type
Business

```html
<!DOCTYPE html>
<html lang="en">
<head>
<meta charset="utf-8">
<title>Brimvoro Technologies – Business Card</title>
<link rel="stylesheet" href="https://fonts.googleapis.com/css2?family=Arimo:wght@700&family=Open+Sans:wght@400;700&family=Tinos:ital,wght@1,700&display=swap">
<style>
  :root {
    --stage: #e8e5e0;
    --ink: #0b0b0b;
    --red: #e41b23;
    --white: #ffffff;
    --paper-top: #ffffff;
    --paper-bottom: #e4e4e4;
    --photo-dark: #1e1e1e;
    --photo-mid: #5e5e5e;
    --photo-light: #8a8a8a;
  }
  * { box-sizing: border-box; margin: 0; padding: 0; }
  html, body { width: 1200px; height: 1015px; overflow: hidden; }
  body {
    background: var(--stage);
    position: relative;
    font-family: "Open Sans", Arial, sans-serif;
  }
  .card {
    position: absolute;
    width: 746px;
    height: 429px;
    border-radius: 22px;
    overflow: hidden;
  }
  .card-front { left: 100px; top: 60px; background: var(--ink); }
  .card-back  { left: 359px; top: 541px; background: linear-gradient(180deg, var(--paper-top), var(--paper-bottom)); }

  .card-shapes { position: absolute; inset: 0; width: 100%; height: 100%; }

  .photo-fill {
    position: absolute; inset: 0;
    background: radial-gradient(ellipse at 35% 45%, var(--photo-light) 0%, var(--photo-mid) 35%, var(--photo-dark) 80%);
  }

  .tagline {
    position: absolute; right: 22px; top: 28px;
    font-family: "Arimo", Arial, sans-serif; font-weight: 700;
    font-size: 23px; color: var(--white);
  }
  .mission {
    position: absolute; left: 118px; top: 162px; width: 600px;
    font-size: 22.5px; line-height: 32px; color: var(--white);
  }
  .address {
    position: absolute; left: 70px; top: 343px;
    font-size: 18px; line-height: 25px; color: var(--white);
  }
  .address-line { padding-left: 22px; position: relative; }
  .address .icon { position: absolute; left: 0; top: 5px; width: 16px; height: 16px; }

  .brand {
    position: absolute; left: 0; right: 0; top: 52px; text-align: center;
  }
  .brand-name {
    font-family: "Open Sans", Arial, sans-serif; font-weight: 700;
    font-size: 100px; line-height: 110px; letter-spacing: -3px; color: var(--ink);
  }
  .brand-sub {
    position: absolute; left: 305px; top: 206px;
    font-size: 20px; color: var(--ink);
  }

  .contact-list {
    position: absolute; left: 61px; top: 297px; list-style: none;
    font-size: 18px; line-height: 25px; color: var(--white);
  }
  .contact-list li { padding-left: 22px; position: relative; }
  .contact-list .icon { position: absolute; left: 0; top: 5px; width: 15px; height: 15px; }

  .person { position: absolute; left: 604px; top: 343px; color: var(--white); }
  .person-name { font-family: "Tinos", "Times New Roman", serif; font-style: italic; font-weight: 700; font-size: 18px; line-height: 24px; }
  .person-title { font-size: 18px; line-height: 24px; }
</style>
</head>
<body>

<section class="card card-front" aria-label="Card front">
  <div class="photo-fill" role="img" aria-label="Abstract dark monochrome photograph"></div>
  <svg class="card-shapes" viewBox="0 0 582 335" preserveAspectRatio="none" aria-hidden="true">
    <path fill="var(--red)" d="M190,0 C240,40 265,72 310,92 C410,126 510,124 582,94 V0 Z"/>
    <path fill="var(--ink)" d="M0,0 H582 V80 C500,116 400,110 300,80 C200,50 90,36 0,62 Z"/>
    <path fill="var(--red)" d="M0,268 C70,232 150,222 220,234 C300,250 350,290 400,335 H0 Z"/>
    <path fill="var(--ink)" d="M0,280 C70,245 150,236 218,247 C296,262 344,298 386,335 H0 Z"/>
  </svg>
  <p class="tagline">Relax. We’ll handle I.T</p>
  <p class="mission">“Brimvoro is committed to delivering the cutting edge technical solutions along with the quality of service that creates&nbsp; clients for life”</p>
  <address class="address" style="font-style:normal">
    <div class="address-line">
      <svg class="icon" viewBox="0 0 16 16" aria-hidden="true"><path fill="var(--white)" d="M8 1 L1 7.5 H3 V15 H6.5 V10.5 H9.5 V15 H13 V7.5 H15 Z"/></svg>
      Brimvoro Technologies Inc
    </div>
    <div class="address-line">48 W. Lantern Ave. Suite 3</div>
    <div class="address-line">Halden, Il 60199</div>
  </address>
</section>

<section class="card card-back" aria-label="Card back">
  <svg class="card-shapes" viewBox="0 0 582 335" preserveAspectRatio="none" aria-hidden="true">
    <path fill="var(--red)" d="M0,222 C80,170 180,168 300,212 C400,250 500,262 582,240 V335 H0 Z"/>
    <path fill="var(--ink)" d="M0,232 C80,182 180,180 300,224 C400,262 500,272 582,252 V335 H0 Z"/>
    <path fill="none" stroke="var(--red)" stroke-width="4" d="M395,272 C445,292 495,318 525,340"/>
  </svg>
  <div class="brand"><span class="brand-name">brimvoro</span></div>
  <p class="brand-sub">Technologies, Inc.</p>

  <ul class="contact-list">
    <li><svg class="icon" viewBox="0 0 16 16" aria-hidden="true"><circle cx="8" cy="8" r="7" fill="none" stroke="var(--white)" stroke-width="1.6"/><path fill="var(--white)" d="M5.5 4 L7 4 L7.5 6 L6.6 6.8 C7 8 8 9 9.2 9.4 L10 8.5 L12 9 L12 10.5 C9 11.5 4.5 7 5.5 4 Z"/></svg>555-210-4471</li>
    <li><svg class="icon" viewBox="0 0 16 16" aria-hidden="true"><rect x="4" y="1.5" width="8" height="4" fill="none" stroke="var(--white)" stroke-width="1.4"/><rect x="1" y="5.5" width="14" height="6" rx="1" fill="var(--white)"/><rect x="4" y="10" width="8" height="4.5" fill="var(--ink)" stroke="var(--white)" stroke-width="1.4"/></svg>Fax: 555.210.4472</li>
    <li><svg class="icon" viewBox="0 0 16 16" aria-hidden="true"><rect x="1" y="3.5" width="14" height="9" fill="none" stroke="var(--white)" stroke-width="1.5"/><path d="M1 3.5 L8 9 L15 3.5" fill="none" stroke="var(--white)" stroke-width="1.5"/></svg>marenholt@brimvoro.com</li>
    <li><svg class="icon" viewBox="0 0 16 16" aria-hidden="true"><circle cx="8" cy="8" r="6.8" fill="none" stroke="var(--white)" stroke-width="1.4"/><ellipse cx="8" cy="8" rx="3" ry="6.8" fill="none" stroke="var(--white)" stroke-width="1.2"/><path d="M1.2 8 H14.8 M2.5 4.5 H13.5 M2.5 11.5 H13.5" stroke="var(--white)" stroke-width="1.1"/></svg>www.brimvoro.com</li>
  </ul>

  <div class="person">
    <p class="person-name">Maren Holt</p>
    <p class="person-title">President</p>
  </div>
</section>

</body>
</html>
```